Event Poster Design for Camp for Teenagers

I need graphics designed for our summer camps event. These camps are for teenagers, 6-12th grades. Primary graphic design is for a 11x17 poster but will also need the images resized for social, 16x9 title slide, and a postcard size. Graphic should include the following:Main Title: Ridgeway Youthline Summer CampsDates: High School - June 3-7; Middle School - June 17-21; Merge - June 24 - 28Register at SDNextGen.comFor each camp, include name and headshot of speaker:High: Liam Brevik (guy in blue shirt)Middle: Marla Penhow (girl)Merge: Joey SilvaInclude Ridgeway Youthline logoBlack Hills Retreat Center, Deadwood, SDGraphic should be attractive to teenagers. Ideas - geometric shapes, 90's coloring/imagery, bright colors, soft earth tones, etc. Open to ideasMy graphic design experience is VERY limited. I will need help receiving the files I need in the various sizes. Thank you.

```html
<!DOCTYPE html>
<html lang="en">
<head>
<meta charset="utf-8">
<title>Ridgeway Youthline Summer Camps 2019</title>
<link rel="stylesheet" href="https://fonts.googleapis.com/css2?family=Titan+One&family=Poppins:wght@500;700;800&family=Montserrat:wght@700;800&display=swap">
<style>
  :root{
    --page:#ececec;
    --white:#ffffff;
    --navy:#3a4a9c;
    --cyan:#34bdec;
    --orange:#ea5f2f;
    --orange-deep:#d6482a;
    --pink:#e8407e;
    --yellow:#f7b235;
    --photo-a:#6f8d74;
    --photo-b:#3b3434;
    --photo-c:#8f8a86;
  }
  html,body{margin:0;padding:0;overflow:hidden}
  body{width:1200px;height:800px;background:var(--page);position:relative}
  .poster{position:absolute;left:336px;top:22px;width:528px;height:756px;display:block;
    box-shadow:0 2px 10px rgba(0,0,0,.12)}
  .bg{fill:var(--white)}
  .navy{fill:var(--navy)} .cyan{fill:var(--cyan)} .orange{fill:var(--orange)}
  .pink{fill:var(--pink)} .white{fill:var(--white)}
  .title{font-family:"Titan One",sans-serif;fill:var(--white);text-anchor:middle}
  .title-small{font-size:26px;letter-spacing:.5px}
  .title-year{font-size:68px}
  .brand{font-family:"Montserrat",sans-serif;font-weight:800;fill:var(--navy);font-size:22px}
  .register-lead{font-family:"Montserrat",sans-serif;font-weight:800;fill:var(--orange);font-size:20px}
  .register-url{font-family:"Montserrat",sans-serif;font-weight:800;fill:var(--navy);font-size:24px}
  .tag-text{font-family:"Poppins",sans-serif;font-weight:500;fill:var(--white);font-size:11.5px;text-anchor:middle;letter-spacing:.4px}
  .speaker{font-family:"Poppins",sans-serif;font-weight:800;font-size:15px;text-anchor:middle}
  .speaker.high{fill:var(--navy)} .speaker.middle{fill:var(--white)} .speaker.merge{fill:var(--white)}
  .date{font-family:"Poppins",sans-serif;font-weight:700;font-size:10px;text-anchor:middle}
  .date.high{fill:var(--navy)} .date.middle{fill:var(--pink)} .date.merge{fill:var(--orange-deep)}
  .venue{font-family:"Montserrat",sans-serif;font-weight:700;fill:var(--navy);font-size:13px}
  .photo-frame{fill:var(--white)}
</style>
</head>
<body>
<svg class="poster" viewBox="0 0 478 685" xmlns="http://www.w3.org/2000/svg" aria-label="Ridgeway Youthline Summer Camps 2019 poster">
  <defs>
    <linearGradient id="art-tones" x1="0" y1="0" x2="1" y2="1">
      <stop offset="0" stop-color="#ea5f2f"/>
      <stop offset=".35" stop-color="#f7b235"/>
      <stop offset=".7" stop-color="#e8407e"/>
      <stop offset="1" stop-color="#3a4a9c"/>
    </linearGradient>
  </defs>
  <rect class="bg" width="478" height="685"/>

  <path class="navy title-panel" d="M175,0 H478 V170 H255 A80,80 0 0 1 175,90 Z"/>

  <rect class="feature-art" x="13" y="182" width="457" height="128" rx="4" fill="url(#art-tones)" opacity=".9"
        role="img" aria-label="Decorative artwork of bright geometric shapes"/>

  <polygon class="cyan band" points="4,402 432,342 478,672 0,660"/>
  <polygon class="white" points="0,643 478,672 478,685 0,685"/>
  <polygon class="orange" points="0,667 300,685 0,685"/>

  <g class="brand-block">
    <text class="brand" x="28" y="52">Ridgeway</text>
    <text class="brand" x="28" y="78">Youthline</text>
  </g>

  <g class="headline">
    <text class="title title-small" x="328" y="54">SUMMER CAMPS</text>
    <text class="title title-year" x="330" y="127">2019</text>
  </g>

  <g class="registration" transform="rotate(-7 13 360)">
    <text class="register-lead" x="13" y="358">REGISTER AT</text>
    <text class="register-url" x="13" y="388">RIDGEWAYYOUTHLINE.COM</text>
  </g>

  <g class="camp camp-high">
    <rect class="navy" x="22" y="407" width="130" height="37"/>
    <text class="tag-text" x="87" y="422">For</text>
    <text class="tag-text" x="87" y="436">High-School</text>
    <rect class="photo-frame" x="32" y="451" width="122" height="146"/>
    <rect x="35" y="454" width="116" height="140" fill="var(--photo-a)" role="img" aria-label="Headshot of speaker Liam Brevik"/>
    <text class="speaker high" x="93" y="613">Liam Brevik</text>
    <rect class="white" x="34" y="619" width="118" height="26"/>
    <text class="date high" x="93" y="630">: Date :</text>
    <text class="date high" x="93" y="641">3-7 June, 2019</text>
  </g>

  <g class="camp camp-middle">
    <rect class="pink" x="170" y="407" width="130" height="37"/>
    <text class="tag-text" x="235" y="422">For</text>
    <text class="tag-text" x="235" y="436">Middle-School</text>
    <rect class="photo-frame" x="176" y="451" width="122" height="146"/>
    <rect x="179" y="454" width="116" height="140" fill="var(--photo-b)" role="img" aria-label="Headshot of speaker Marla Penhow"/>
    <text class="speaker middle" x="237" y="613">Marla Penhow</text>
    <rect class="white" x="178" y="619" width="118" height="26"/>
    <text class="date middle" x="237" y="630">: Date :</text>
    <text class="date middle" x="237" y="641">17-21 June, 2019</text>
  </g>

  <g class="camp camp-merge">
    <rect class="orange" x="317" y="407" width="130" height="37"/>
    <text class="tag-text" x="382" y="422">For</text>
    <text class="tag-text" x="382" y="436">Merge-School</text>
    <rect class="photo-frame" x="320" y="451" width="122" height="146"/>
    <rect x="323" y="454" width="116" height="140" fill="var(--photo-c)" role="img" aria-label="Headshot of speaker Danny Obert"/>
    <text class="speaker merge" x="381" y="613">Danny Obert</text>
    <rect class="white" x="322" y="619" width="118" height="26"/>
    <text class="date merge" x="381" y="630">: Date :</text>
    <text class="date merge" x="381" y="641">24-28 June, 2019</text>
  </g>

  <text class="venue" x="8" y="660" transform="rotate(3.5 8 660)">Cedar Fork Retreat Center, Alder Springs, SD</text>
</svg>
</body>
</html>
```